"Drink Champagne and Dance on the Table" sort of business card needed!

We throw events, weddings, engagement parties, baby showers and the sort of end of year corporate events that people remember long after the glitter has settled - the sort of events that make you stand still and say wow when you walk in and then make you want to "Drink Champagne and Dance on the Tables"

We have a great logo with heaps of potential and need a business card that just screams creative professionals!

We are based in Auckland, NZ and are priced at the Premium end of the market were there are around 10 other main competitors. We need to stand out and make a strong statement about who we are!

Our Business Card will be one of the few items that we print out so are fully prepared to invest in a premium print job.

We really love our logo and think it has heaps of potential! Its ok if you would like to manipulate it (maybe put it on an angle, or use the circle element on its own?).

Black and Gold is very striking, but its very done in our market so we would like to avoid a solid black background please

We have done a bit of an inspiration document to give you an idea of the sort of look and feel we are hoping to achieve.

Target Market(s)

Woman aged 30 - 45 with an income bracket of $70k +

Industry/Entity Type

Event Planning

Contact Information for Business Card

Marnie
hello@fennwhistle.co.nz
www.fennwhistle.co.nz
02739418207

Number of Pages Required

5+ page

Requirements
Must have
• Vibrant colours and design (we love the vibrant pink and gold in the inspiration file)
• We would love to see some colour and creativity (although the black and gold is very striking). Because we are doing such minimal print work I am happy for the cards to be a little more expensive so if you want to use cut outs, rounded corners, gold foil, non standard size etc I am happy for that too. I really want the wow factor.
Nice to have
• We would like the design to be double sided.
Should not have
• The logo colour changed
• Use of Purple or Green or solid black background.
• Wedding Photos!

```html
<!DOCTYPE html>
<html lang="en">
<head>
<meta charset="utf-8">
<title>Fenn and Whistle – Business Card</title>
<link href="https://fonts.googleapis.com/css2?family=Libre+Baskerville&family=Pacifico&display=swap" rel="stylesheet">
<style>
  :root {
    --page-bg: #ececec;
    --gold-deep: #c4963e;
    --gold-mid: #e4c67a;
    --gold-light: #f8ecbf;
    --glitter-strong: rgba(246, 200, 20, 0.85);
    --glitter-soft: rgba(246, 200, 20, 0);
    --brand-gold: #b58c2e;
    --ink: #141210;
  }
  * { box-sizing: border-box; margin: 0; padding: 0; }
  html, body { width: 1200px; height: 900px; overflow: hidden; }
  body {
    background: var(--page-bg);
    position: relative;
    font-family: "Libre Baskerville", Georgia, serif;
  }
  .card {
    position: absolute;
    top: 301px;
    width: 520px;
    height: 297px;
    overflow: hidden;
    background: linear-gradient(180deg, var(--gold-deep) 0%, var(--gold-mid) 32%, var(--gold-light) 50%, var(--gold-mid) 70%, var(--gold-deep) 100%);
    box-shadow: 0 6px 18px rgba(0, 0, 0, 0.12);
  }
  .card--front { left: 50px; }
  .card--back { left: 630px; }
  .glitter {
    position: absolute;
    inset: 0;
    background:
      radial-gradient(ellipse 38% 75% at 100% 35%, var(--glitter-strong), var(--glitter-soft) 75%),
      radial-gradient(ellipse 55% 40% at 30% 100%, var(--glitter-strong), var(--glitter-soft) 75%),
      radial-gradient(ellipse 30% 30% at 78% 95%, rgba(246, 200, 20, 0.6), var(--glitter-soft) 75%);
  }
  .brand {
    position: absolute;
    left: 0; right: 0; top: 44px;
    display: flex;
    flex-direction: column;
    align-items: center;
    color: var(--brand-gold);
  }
  .brand__circle {
    width: 100px; height: 100px;
    border: 3px solid var(--brand-gold);
    border-radius: 50%;
  }
  .brand__name {
    margin-top: 22px;
    font-family: "Libre Baskerville", Georgia, serif;
    font-size: 32px;
    line-height: 1;
  }
  .contact {
    position: absolute;
    left: 56px; top: 52px;
    color: var(--ink);
  }
  .contact__name {
    font-family: "Pacifico", cursive;
    font-weight: 400;
    font-size: 50px;
    line-height: 1.1;
    margin-bottom: 10px;
  }
  .contact__list { list-style: none; }
  .contact__item {
    display: flex;
    align-items: center;
    gap: 10px;
    font-size: 14px;
    line-height: 26px;
  }
  .contact__icon { width: 16px; height: 16px; flex: none; }
</style>
</head>
<body>
  <section class="card card--front" aria-label="Card front">
    <div class="glitter" role="img" aria-label="Scattered gold glitter speckles"></div>
    <div class="brand">
      <div class="brand__circle"></div>
      <div class="brand__name">Fenn and Whistle</div>
    </div>
  </section>

  <section class="card card--back" aria-label="Card back">
    <div class="glitter" role="img" aria-label="Scattered gold glitter speckles"></div>
    <div class="contact">
      <h1 class="contact__name">Marnie</h1>
      <ul class="contact__list">
        <li class="contact__item">
          <svg class="contact__icon" viewBox="0 0 16 16" fill="none" stroke="currentColor" stroke-width="1.2"><rect x="1.5" y="3.5" width="13" height="9"/><path d="M1.5 3.5 8 9l6.5-5.5"/></svg>
          hello@fennwhistle.co.nz
        </li>
        <li class="contact__item">
          <svg class="contact__icon" viewBox="0 0 16 16" fill="none" stroke="currentColor" stroke-width="1.2"><circle cx="8" cy="8" r="6.5"/><ellipse cx="8" cy="8" rx="3" ry="6.5"/><path d="M1.5 8h13M2.5 5h11M2.5 11h11"/></svg>
          www.fennwhistle.co.nz
        </li>
        <li class="contact__item">
          <svg class="contact__icon" viewBox="0 0 16 16" fill="none" stroke="currentColor" stroke-width="1.2"><circle cx="8" cy="8" r="7"/><path d="M5.2 3.8c.3-.2.7-.2.9.1l1 1.4c.2.3.2.7-.1.9l-.6.5c.5 1.1 1.3 2 2.4 2.6l.5-.6c.2-.3.6-.3.9-.1l1.4 1c.3.2.3.6.1.9l-.7.9c-.3.4-.9.5-1.4.3C7.2 11.6 5 9.3 4.2 6.9c-.2-.5 0-1 .3-1.4z" fill="currentColor" stroke="none"/></svg>
          02739418207
        </li>
      </ul>
    </div>
  </section>
</body>
</html>
```